Fernleaf Yards needs a brochure

I need to put together a booklet type brochure visually describing what I do. I would like the brochure to have the same elegance as the logo and the business card. I envision using the green design from the back of the business card, on the back of the brochure as well. I would like to have a space for an "About Us" area in which I can explain about the evolution of Fernleaf Yards. I would also like to have pictures of work that I have completed. I will send you both copy and photos. I would like the brochure to print matte and be an unusual shape - like a square booklet instead of the normal 8.5x11. I would also like to include the logos of the organizations that I am a member of - NHRO, TIMBER, KWOE.
Having some trouble uploading with internet explorer. Will fix the problem and upload ASAP. Thank you all for your patience.

```html
<!DOCTYPE html>
<html lang="en">
<head>
<meta charset="utf-8">
<title>Fernleaf Yards — Brochure</title>
<link rel="stylesheet" href="https://fonts.googleapis.com/css2?family=Source+Sans+3:wght@400;600;700&display=swap">
<style>
  :root {
    --leaf: #8dc63f;
    --leaf-deep: #7ab32e;
    --paper: #ffffff;
    --ink: #2f2f2f;
    --soil: #8a4a3a;
    --backdrop: #ecebe6;
    --badge-pink: #e8448f;
    --badge-blue: #2a8fd0;
    --badge-green: #4f8f3a;
  }
  * { box-sizing: border-box; margin: 0; padding: 0; }
  html, body { width: 1200px; height: 1000px; overflow: hidden; }
  body {
    background: var(--backdrop);
    font-family: "Source Sans 3", Arial, sans-serif;
    color: var(--ink);
    position: relative;
  }
  .page {
    position: absolute;
    background: var(--paper);
    overflow: hidden;
    box-shadow: 0 2px 8px rgba(0,0,0,.12);
  }
  .page svg.shapes { position: absolute; inset: 0; width: 100%; height: 100%; }
  .photo { position: absolute; }

  /* Front cover */
  .front-cover { left: 140px; top: 30px; width: 460px; height: 460px; }
  .front-cover .photo {
    left: 0; top: 20px; width: 460px; height: 370px;
    background: linear-gradient(160deg, #2f5a2a 0%, #3f7a36 35%, #d89aae 55%, #e9e1a0 75%, #b7b2d8 100%);
  }
  .logo-box {
    position: absolute; left: 292px; top: 42px; width: 140px; height: 100px;
    background: var(--paper);
    display: flex; flex-direction: column; align-items: center; justify-content: center; gap: 8px;
  }
  .logo-mark { width: 26px; height: 26px; border-radius: 50%; background: var(--leaf); }
  .brand-name { font-weight: 600; color: var(--soil); font-size: 17px; white-space: nowrap; }
  .tagline {
    position: absolute; left: 40px; bottom: 26px;
    color: var(--paper); font-size: 9.5px; letter-spacing: 5px; text-transform: uppercase;
  }

  /* Inside spread */
  .inside-spread { left: 140px; top: 510px; width: 920px; height: 460px; }
  .inside-spread .photo-left {
    left: 0; top: 0; width: 460px; height: 460px;
    background: linear-gradient(170deg, #7c7f7c 0%, #9a968d 30%, #2e3a2c 55%, #c2ad8c 80%, #a8aea4 100%);
  }
  .inside-spread .photo-right {
    left: 460px; top: 0; width: 205px; height: 460px;
    background: linear-gradient(180deg, #9b5a48 0%, #c99bc9 30%, #3f6b35 55%, #e0a0b8 70%, #ece4b0 82%, #8a8fd0 100%);
  }
  .about {
    position: absolute; left: 682px; top: 26px; width: 222px;
  }
  .about h2 {
    color: var(--leaf); font-weight: 700; font-size: 12.5px; line-height: 1.2; margin-bottom: 10px;
  }
  .about p { font-size: 8.6px; line-height: 1.5; margin-bottom: 7px; }
  .spread-wordmark {
    position: absolute; left: 60px; top: 370px;
    font-size: 74px; font-weight: 600; color: rgba(255,255,255,.32); white-space: nowrap;
    transform: rotate(-4deg); transform-origin: left bottom;
  }
  .services {
    position: absolute; left: 40px; bottom: 12px;
    color: var(--paper); font-size: 10px; letter-spacing: .3px;
  }
  .spread-brand {
    position: absolute; right: 16px; top: 366px;
    display: flex; align-items: center; gap: 6px;
    color: var(--paper); font-weight: 600; font-size: 11px;
  }
  .spread-brand .dot { width: 14px; height: 14px; border-radius: 50%; background: var(--paper); }

  /* Back cover */
  .back-cover { left: 600px; top: 30px; width: 460px; height: 460px; }
  .back-logo {
    position: absolute; right: 40px; top: 300px;
    display: flex; flex-direction: column; align-items: center; gap: 10px;
  }
  .member-badges {
    position: absolute; left: 22px; bottom: 30px; display: flex; gap: 12px; align-items: center;
  }
  .badge { display: block; }
  .badge-box { width: 56px; height: 22px; border: 1.5px solid var(--badge-pink); }
  .badge-round { width: 22px; height: 22px; border-radius: 50%; background: var(--badge-blue); }
  .badge-square { width: 24px; height: 24px; background: var(--badge-green); }
  .contact {
    position: absolute; right: 22px; bottom: 34px; font-size: 8.5px; color: var(--leaf-deep);
  }
  .contact b { font-weight: 700; }
</style>
</head>
<body>

<section class="page front-cover" aria-label="Front cover">
  <div class="photo" role="img" aria-label="Photo of a planted bed with pink calla lilies and pale yellow and violet pansies"></div>
  <svg class="shapes" viewBox="0 0 460 460" aria-hidden="true">
    <path d="M0 0 H460 V22 Q240 62 0 34 Z" fill="var(--leaf)"/>
    <path d="M0 38 Q240 66 460 26" fill="none" stroke="#fff" stroke-width="3"/>
    <path d="M0 372 Q220 330 460 352 V460 H0 Z" fill="var(--leaf)"/>
    <path d="M0 368 Q220 326 460 348" fill="none" stroke="#fff" stroke-width="3"/>
  </svg>
  <div class="logo-box">
    <span class="logo-mark"></span>
    <span class="brand-name">Fernleaf Yards</span>
  </div>
  <p class="tagline">Local, Sustainabl, Healthy, Elegant</p>
</section>

<section class="page back-cover" aria-label="Back cover">
  <svg class="shapes" viewBox="0 0 460 460" aria-hidden="true">
    <path d="M0 0 H460 V120 Q260 250 0 180 Z" fill="var(--leaf)"/>
  </svg>
  <div class="back-logo">
    <span class="logo-mark"></span>
    <span class="brand-name">Fernleaf Yards</span>
  </div>
  <div class="member-badges" aria-label="Member organisations: KWOE, TIMBER, NHRO">
    <span class="badge badge-box" role="img" aria-label="KWOE membership badge"></span>
    <span class="badge badge-round" role="img" aria-label="TIMBER membership badge"></span>
    <span class="badge badge-square" role="img" aria-label="NHRO membership badge"></span>
  </div>
  <p class="contact"><b>Phone:</b> 555-014-2290 <b>Email:</b> hello@fernleafyards.example</p>
</section>

<section class="page inside-spread" aria-label="Inside spread">
  <div class="photo photo-left" role="img" aria-label="Photo of tall dark planters filled with white flowers on a gravel terrace"></div>
  <div class="photo photo-right" role="img" aria-label="Photo of pink foxgloves rising above calla lilies and pansies by a brick wall"></div>
  <article class="about">
    <h2>Uscerfir isquamei consuam horit, fatum denium et gra? Ostilinequi condem aciemul occhui ponditi ngulica et; nermius Cast Opio publica dum untem horus. Ede lat ursuliam movivil unum</h2>
    <p>omnem pulium optea essusqua nontruncupio iam is movere, caverum ina noximis con pere, se, que ium ia L. Maequos imistrum et vividees fachuct ustinci usquam hortium aur. Valictum nos anditam nihil con vignat vis, nocrum oreis­sena, fecribemus, us, P. cavoc ma, no. Det ad re nu vast pl. Ad nonsimus cia nostori sendes actur la ca vitius or unu mor am quiusse cerem. Verica macipte batuus redem pra auctodi eri­dete, omnitam urimuro escem dicibus. Moracte beffrei sent.</p>
    <p>Em is Ad sula pl. Maritius, non tenate confec faci inum inpror am antra inum omnitab unu­labe mquit; int? Maionste culturo Catrum dium derrituus ad laetisque ius auctu quitem essu­liae, ne noste, trus; Cas forum hicia? Rac tea perum por qua re mena, Catimusque nonfiri patiam cont? Hum tast Cuppi. It et factura ripti,</p>
  </article>
  <svg class="shapes" viewBox="0 0 920 460" aria-hidden="true">
    <path d="M0 418 Q420 330 920 352 V460 H0 Z" fill="var(--leaf)"/>
    <path d="M0 414 Q420 326 920 348" fill="none" stroke="#fff" stroke-width="3"/>
  </svg>
  <div class="spread-wordmark">Fernleaf Yards</div>
  <p class="services">Container Design &amp; Installation &nbsp;·&nbsp; Vegetable garden Design &amp; Installation</p>
  <div class="spread-brand"><span class="dot"></span>Fernleaf Yards</div>
</section>

</body>
</html>
```